Hurricane Damage Public Adjuster Billboard

I have created several projects with you and have several great designs. I need to format them into a Billboard for upcoming Hurricane Season. Need done in a month. Im also in process of getting an eye catching and easy to remember 800# Vanity phone number like Call 800-Stormfix or 800- Need Help? My included past Sketch Guild projects will give you an idea of what colors, schemes, and designs I gravitate towards. 3 past Design projects were 1) 2 Logos where I picked the 1st place and the 2nd place and 2) Index Card where I picked the winner as the Index Card and the 2nd place as a Post Card. Point is, I will pick and pay for 2 winners if they're good. This should help to sweeten the pot. Also, please look at my website for ideas that I like:

www.TheClaimWardenGroup.com
I want people to feel that I am the best and highest. Level.

I've been getting a lot of quick half effort designs basically cut & pasting my previous projects. Please don't rush and take your time to be creative. A an example, my Biggest Competitor is Crestline Public Adjusting. Their colors are Black and Gold while mine are Blue, White, and Black with a highlight of Orange if possible. I JUST imported a picture of their BillBoard. I need mine better and BLOW AWAY THEIRS. Terms like "Don't be Victimized Twice ?, Don't let the Hurricane Ruin your Life?". "Get Fairly Paid & Move On" "Our Clients Claims are VIP?
Updates

I'm getting a lot of quick half effort ones. I'd rather you take your time and really put some thoughts and effort into it. My Biggest Competitor is Crestline Public Adjusting. They have black & gold colors, while I have Blue, Black, and white.

It needs to blow theirs away. I have imported their Billboard for comparative purposes.

Guy's,
I'll make it easier for you in what I'm looking for. Please look at the Crestline Billboard picture attached.

1) Put my "Blue Shield" to the left, replacing their logo
2) change color patterns from their (Black, Gold, White) to my color schemes of (Black, Blue, White)
3) I want to see my name where their is:

THE
Claim Warden Group
EXPERT & LOCAL Public Adjusters
"FOR THE POLICYHOLDER!!"

4) to the right, add the A+Rated logo and QTR+ Accredited logo, 5 Star Zentrio Rated logo, 5 Start BLOCKLINK Highly Rated logo, etc..

5) the right side is where you can be creative as I will not have a picture of me there.

"20+ Years of Experience, Recovering Millions for our VIP Clients"

"Your Best, Locally-Based Private Adjuster & Advocate'
"FOR THE POLICYHOLDER!!"

"Don't be victimized Twice!!"

"Don't let the Hurricane Ruin Your Life!!"

This should really help. Also, refer to my website, maybe a couple testimonial fillers?

Thanks all,

marvin@TheClaimWardenGroup.com

Just imported a few awards that would look great to the right side with all the other 5 Star Ratings and accolades.
This right section could be titled like zmy Website:

5 Star Reviews, Ratings & Awards:
4-5 Logos underneath?

Target Market(s)

Coastal place where a Hurricane 🌀 🌀 Hits

Industry/Entity Type

Hurricane Public Insurance Adjuster

Font styles to use
Sans Serif
Other font styles liked:
• Calvera fonts

Colors
0054AA
0677BA
7BADD7
CADEEF
E8F1F8
EE7325
F08F49
F5BC92
FAE3D3
FDF4ED

Requirements
Must have
• Use my past project logos, colors, and schemes to create eye grabbing BillBoard
Nice to have
Should not have
• Not be too busy, must be Easy to Read, Eye Catchy

```html
<!DOCTYPE html>
<html lang="en">
<head>
<meta charset="utf-8">
<title>The Claim Warden Group – Hurricane Season Billboard</title>
<link rel="stylesheet" href="https://fonts.googleapis.com/css2?family=Montserrat:ital,wght@0,600;0,700;1,700&family=Barlow+Condensed:wght@600;700&display=swap">
<style>
  :root {
    --page: #d4d4d4;
    --storm-dark: #18222e;
    --storm-mid: #34404f;
    --brand-blue: #1f9ae0;
    --panel-blue: #1478b8;
    --panel-deep: #0b4c7a;
    --band-blue: #134d77;
    --alert-red: #d71f27;
    --alert-red-text: #e3141c;
    --white: #ffffff;
    --badge-white: #f7f7f7;
  }
  html, body {
    margin: 0;
    padding: 0;
    width: 1072px;
    height: 1200px;
    overflow: hidden;
    background: var(--page);
  }
  .billboard {
    position: absolute;
    left: 36px;
    top: 391px;
    width: 1000px;
    height: 418px;
    overflow: hidden;
    box-shadow: 0 10px 22px rgba(0,0,0,.45);
    font-family: "Montserrat", sans-serif;
    color: var(--white);
  }
  .storm-scene {
    position: absolute;
    inset: 0;
    background:
      radial-gradient(ellipse at 70% 85%, rgba(120,110,100,.55), transparent 55%),
      radial-gradient(ellipse at 50% 40%, rgba(110,125,145,.5), transparent 60%),
      linear-gradient(160deg, var(--storm-dark) 0%, var(--storm-mid) 55%, #2a2f36 100%);
  }
  .shapes { position: absolute; inset: 0; }
  .brand {
    position: absolute;
    left: 27px;
    top: 28px;
    display: flex;
    align-items: center;
    gap: 12px;
  }
  .brand-mark {
    width: 18px;
    height: 18px;
    background: var(--brand-blue);
  }
  .brand-name {
    font-weight: 700;
    font-size: 24px;
    letter-spacing: 1px;
    color: var(--brand-blue);
  }
  .brand-line {
    position: absolute;
    left: 57px;
    top: 72px;
    font-size: 13px;
    font-weight: 600;
    letter-spacing: 3px;
  }
  .brand-tagline {
    position: absolute;
    left: 57px;
    top: 95px;
    font-size: 17px;
    font-weight: 700;
    font-style: italic;
    letter-spacing: 1px;
  }
  .headline {
    position: absolute;
    left: 24px;
    top: 153px;
    font-family: "Barlow Condensed", sans-serif;
    font-weight: 700;
    font-size: 52px;
    line-height: 1;
    text-shadow: 2px 2px 0 #000;
  }
  .promise {
    position: absolute;
    left: 22px;
    top: 241px;
    font-size: 29px;
    font-weight: 700;
    line-height: 40px;
  }
  .email {
    position: absolute;
    left: 28px;
    top: 351px;
    height: 46px;
    display: flex;
    align-items: center;
    gap: 14px;
    font-size: 20px;
    font-weight: 600;
  }
  .warning {
    position: absolute;
    right: 27px;
    top: 28px;
    text-align: right;
    font-size: 36px;
    font-weight: 700;
    line-height: 39px;
  }
  .phone {
    position: absolute;
    left: 625px;
    top: 118px;
    height: 73px;
    display: flex;
    align-items: center;
    gap: 24px;
    font-size: 44px;
    font-weight: 700;
  }
  .experience {
    position: absolute;
    left: 617px;
    top: 204px;
    width: 370px;
    text-align: center;
    font-family: "Barlow Condensed", sans-serif;
  }
  .experience-years {
    font-size: 42px;
    font-weight: 700;
    color: var(--alert-red-text);
    line-height: 44px;
    text-shadow: 1px 1px 0 #000;
  }
  .experience-detail {
    font-size: 24px;
    font-weight: 600;
    line-height: 28px;
  }
  .badge {
    position: absolute;
    top: 350px;
    height: 47px;
    background: var(--badge-white);
    border-radius: 2px;
  }
  .badge-rating { left: 520px; width: 104px; border: 2px solid var(--alert-red); box-sizing: border-box; }
  .badge-accredit { left: 635px; width: 120px; background: var(--panel-blue); }
  .badge-reviews { left: 765px; width: 105px; border: 2px solid var(--alert-red); box-sizing: border-box; }
  .badge-community { left: 882px; width: 104px; border: 2px solid #2d7cc0; box-sizing: border-box; }
  .badge-caption {
    position: absolute;
    left: 635px;
    top: 400px;
    width: 120px;
    text-align: center;
    font-size: 9px;
    font-weight: 700;
  }
</style>
</head>
<body>
  <section class="billboard">
    <div class="storm-scene" role="img" aria-label="Stormy sky with lightning over a flat rural field"></div>

    <svg class="shapes" width="1000" height="418" viewBox="0 0 1000 418" aria-hidden="true">
      <defs>
        <linearGradient id="panelFill" x1="0" y1="0" x2="0" y2="1">
          <stop offset="0" stop-color="#2a9ad8"/>
          <stop offset="0.55" stop-color="#1271ad"/>
          <stop offset="1" stop-color="#0c5183" stop-opacity="0"/>
        </linearGradient>
        <linearGradient id="redFill" x1="0" y1="0" x2="1" y2="0">
          <stop offset="0" stop-color="#c81a20"/>
          <stop offset="0.7" stop-color="#d91f26"/>
          <stop offset="1" stop-color="#d91f26" stop-opacity="0"/>
        </linearGradient>
        <linearGradient id="phoneFill" x1="0" y1="0" x2="0" y2="1">
          <stop offset="0" stop-color="#0b4c7a"/>
          <stop offset="1" stop-color="#0e5e95"/>
        </linearGradient>
        <clipPath id="panelClip">
          <path d="M558 0 C540 90 560 190 650 290 L1000 290 L1000 0 Z"/>
        </clipPath>
      </defs>
      <path d="M558 0 C540 90 560 190 650 290 L1000 290 L1000 0 Z" fill="url(#panelFill)"/>
      <rect x="540" y="118" width="460" height="73" fill="url(#phoneFill)" clip-path="url(#panelClip)"/>
      <polygon points="0,229 600,229 700,333 0,333" fill="url(#redFill)"/>
      <rect x="0" y="351" width="530" height="46" fill="#134d77" opacity="0.92"/>
    </svg>

    <div class="brand">
      <span class="brand-mark"></span>
      <span class="brand-name">THE CLAIM WARDEN GROUP</span>
    </div>
    <div class="brand-line">INSURANCE CLAIM EXPERTS</div>
    <div class="brand-tagline">“FOR THE POLICYHOLDER!”</div>

    <div class="headline">FOR THE POLICYHOLDER!!</div>
    <div class="promise">Your Best, Locally-Based Private<br>Adjuster &amp; Advocate</div>

    <div class="email">
      <svg width="28" height="20" viewBox="0 0 28 20" aria-hidden="true">
        <rect x="1" y="1" width="26" height="18" fill="none" stroke="#fff" stroke-width="2"/>
        <path d="M1 1 L14 11 L27 1 M1 19 L11 9 M27 19 L17 9" fill="none" stroke="#fff" stroke-width="2"/>
      </svg>
      <span>marvin@TheClaimWardenGroup.com</span>
    </div>

    <div class="warning">Don't let the Hurric<br>ane Ruin Your Life</div>

    <div class="phone">
      <svg width="42" height="42" viewBox="0 0 24 24" aria-hidden="true">
        <path fill="#fff" d="M6.6 10.8a15.1 15.1 0 0 0 6.6 6.6l2.2-2.2a1 1 0 0 1 1-.25 11.4 11.4 0 0 0 3.6.57 1 1 0 0 1 1 1V20a1 1 0 0 1-1 1A17 17 0 0 1 3 4a1 1 0 0 1 1-1h3.5a1 1 0 0 1 1 1c0 1.25.2 2.45.57 3.57a1 1 0 0 1-.25 1z"/>
        <path fill="none" stroke="#fff" stroke-width="1.6" d="M14 2.5a8 8 0 0 1 7.5 7.5M14 6a4.5 4.5 0 0 1 4 4"/>
      </svg>
      <span>555-013-4827</span>
    </div>

    <div class="experience">
      <div class="experience-years">20+ Years of Experience</div>
      <div class="experience-detail">Recovering Millions for our VIP Clients</div>
    </div>

    <div class="badge badge-rating"></div>
    <div class="badge badge-accredit"></div>
    <div class="badge badge-reviews"></div>
    <div class="badge badge-community"></div>
    <div class="badge-caption">QTR Rating: A+</div>
  </section>
</body>
</html>
```